Business Cards and Stationery- Lumen Quill Studio
Lumen Quill Studio
Business Cards and Stationery- Lumen Quill Studio - Miscellaneous
Creative Brief
Bright & Fun-filled
Marisol Quenby
Chicago, IL
lumen.quill.stdo@brightpost.test
lumen-quill-studio.test
I would like the business cards to just have the above web address and email. I would also like a 4X5 post card with this additional information: Facebook: facebook.com/groups/lumen.quill.studio Instagram: lumen.quill.studio Twitter: @LumenQuillStd Pinterest: pinterest.com/LumenQuillStd/
Not sure if I just want the logo, i'm open to anything

```html
<!DOCTYPE html>
<html lang="en">
<head>
<meta charset="utf-8">
<title>Lumen Quill Studio – Business Cards</title>
<link href="https://fonts.googleapis.com/css2?family=Open+Sans:wght@400;600&display=swap" rel="stylesheet">
<style>
  :root {
    --navy: #1c1a86;
    --navy-deep: #16146e;
    --paper: #ffffff;
    --ink: #3a3a5a;
    --stage: #ecebe8;
  }
  * { margin: 0; padding: 0; box-sizing: border-box; }
  html, body { width: 1200px; height: 904px; overflow: hidden; }
  body {
    background: var(--stage);
    font-family: "Open Sans", Arial, sans-serif;
    position: relative;
  }
  .card {
    position: absolute;
    width: 660px;
    height: 378px;
    border-radius: 4px;
    box-shadow: 0 10px 28px rgba(0,0,0,0.18);
    overflow: hidden;
  }
  .card-front {
    left: 110px; top: 60px;
    background: var(--navy);
    color: var(--paper);
  }
  .card-back {
    left: 430px; top: 466px;
    background: var(--paper);
    color: var(--navy);
  }
  .wordmark {
    display: flex;
    align-items: center;
    gap: 10px;
    font-weight: 600;
    white-space: nowrap;
  }
  .wordmark-dot {
    border-radius: 50%;
    flex: none;
  }
  .card-front .wordmark {
    position: absolute;
    left: 50%; top: 150px;
    transform: translateX(-50%);
    font-size: 34px;
  }
  .card-front .wordmark-dot { width: 16px; height: 16px; background: var(--paper); }
  .front-web {
    position: absolute;
    left: 0; right: 0; bottom: 44px;
    text-align: center;
    font-size: 14px;
    letter-spacing: 0.3px;
  }
  .card-back .wordmark {
    position: absolute;
    left: 28px; top: 70px;
    font-size: 22px;
  }
  .card-back .wordmark-dot { width: 12px; height: 12px; background: var(--navy); }
  .contact-list {
    position: absolute;
    left: 30px; bottom: 34px;
    list-style: none;
    font-size: 13px;
    color: var(--ink);
  }
  .contact-list li {
    display: flex;
    align-items: center;
    gap: 12px;
    height: 22px;
  }
  .contact-list svg { width: 14px; height: 14px; fill: var(--navy); flex: none; }
  .name-panel {
    position: absolute;
    right: 0; top: 0;
    width: 330px; height: 378px;
    background: var(--navy);
    border-radius: 190px 0 0 190px;
    display: flex;
    align-items: center;
    justify-content: center;
  }
  .holder-name {
    color: var(--paper);
    font-size: 17px;
    font-weight: 600;
  }
</style>
</head>
<body>
  <section class="card card-front" aria-label="Business card front">
    <div class="wordmark"><span class="wordmark-dot"></span>Lumen Quill Studio</div>
    <p class="front-web">www.lumen-quill-studio.test</p>
  </section>

  <section class="card card-back" aria-label="Business card back">
    <div class="wordmark"><span class="wordmark-dot"></span>Lumen Quill Studio</div>
    <ul class="contact-list">
      <li>
        <svg viewBox="0 0 24 24" aria-hidden="true"><path d="M12 2a7 7 0 0 0-7 7c0 5.2 7 13 7 13s7-7.8 7-13a7 7 0 0 0-7-7zm0 9.5A2.5 2.5 0 1 1 12 6.5a2.5 2.5 0 0 1 0 5z"/></svg>
        Chicago, IL
      </li>
      <li>
        <svg viewBox="0 0 24 24" aria-hidden="true"><path d="M2 5h20v14H2z M3.5 6.5 12 13l8.5-6.5" fill="none" stroke="#1c1a86" stroke-width="2"/></svg>
        lumen.quill.stdo@brightpost.test
      </li>
      <li>
        <svg viewBox="0 0 24 24" aria-hidden="true"><circle cx="12" cy="12" r="9" fill="none" stroke="#1c1a86" stroke-width="2"/><path d="M3 12h18M12 3c3 3 3 15 0 18M12 3c-3 3-3 15 0 18" fill="none" stroke="#1c1a86" stroke-width="1.6"/></svg>
        www.lumen-quill-studio.test
      </li>
    </ul>
    <div class="name-panel">
      <p class="holder-name">Marisol Quenby</p>
    </div>
  </section>
</body>
</html>
```